High End Business Card Design for Flooring Store

Looking for a new card design for our hardwood flooring company. We have no print budget for these and are open to cards made from wood, metal, cardstock with embossed print ... or any combination of these. No plastic.

We sell luxury products and I want the cards to reflect our image of quality and class.

Our contact information as such;
Employee Name
418 Colbrook Blvd.
Brenton, ON
K9R-3M5
(555) 214-3968
Employee email @velkaflooring.com

Target Market(s)

Home Builders

Contact Information for Business Card

Emnployee name, business contact information

```html
<!DOCTYPE html>
<html lang="en">
<head>
<meta charset="utf-8">
<title>Velka Business Card</title>
<link rel="stylesheet" href="https://fonts.googleapis.com/css2?family=Arimo:wght@400;700&family=Montserrat:wght@400;500&display=swap">
<style>
  :root {
    --backdrop: #dedede;
    --card-white: #f7f7f7;
    --brand-red: #8a2423;
    --brand-gold: #d6a623;
    --ink: #222222;
    --muted: #6b6b6b;
    --rule: #b9b9b9;
    --white: #ffffff;
  }
  * { margin: 0; padding: 0; box-sizing: border-box; }
  html, body { width: 1200px; height: 1040px; overflow: hidden; }
  body { background: var(--backdrop); position: relative; font-family: "Arimo", Arial, sans-serif; }

  .card {
    position: absolute;
    left: 284px;
    width: 644px;
    border-radius: 18px;
    overflow: hidden;
  }
  .card-front { top: 130px; height: 366px; background: var(--card-white); }
  .card-back { top: 568px; height: 368px; background: var(--brand-gold); }

  .brand { position: absolute; text-align: center; font-family: "Montserrat", Arial, sans-serif; }
  .brand-name { display: flex; align-items: center; justify-content: center; gap: 8px; color: var(--brand-red); font-weight: 500; line-height: 1; }
  .brand-mark { display: inline-block; }
  .brand-tagline { line-height: 1.2; }

  .card-front .brand { left: 84px; top: 156px; width: 224px; }
  .card-front .brand-name { font-size: 54px; }
  .card-front .brand-mark { width: 26px; height: 26px; background: var(--brand-gold); }
  .card-front .brand-tagline { font-size: 14px; color: var(--muted); margin-top: 2px; }

  .divider { position: absolute; left: 322px; top: 102px; width: 1px; height: 184px; background: var(--rule); }

  .contact { position: absolute; left: 341px; top: 96px; color: var(--ink); }
  .contact-name { font-size: 26px; font-weight: 700; color: var(--brand-red); line-height: 1.1; }
  .contact-title { font-size: 16px; color: var(--brand-gold); margin-left: 2px; margin-top: 1px; }
  .contact-address { font-size: 16px; line-height: 20px; margin-top: 12px; }
  .contact-lines { list-style: none; margin-top: 8px; font-size: 16px; line-height: 20px; }
  .contact-lines li { display: flex; align-items: center; gap: 8px; }
  .contact-lines svg { width: 14px; height: 14px; flex: none; }

  .card-band { position: absolute; left: 0; bottom: 0; width: 644px; height: 18px; }

  .card-back .brand { left: 0; top: 112px; width: 644px; }
  .card-back .brand-name { font-size: 100px; gap: 16px; }
  .card-back .brand-mark { width: 56px; height: 56px; background: var(--white); }
  .card-back .brand-tagline { font-size: 24px; color: var(--white); margin-top: -6px; line-height: 26px; }
</style>
</head>
<body>

<section class="card card-front">
  <div class="brand">
    <div class="brand-name"><span class="brand-mark"></span>Velka</div>
    <div class="brand-tagline">Planchers &amp; Escaliers<br>Flooring &amp; Stairs</div>
  </div>

  <div class="divider"></div>

  <div class="contact">
    <div class="contact-name">Alex Bernard</div>
    <div class="contact-title">President</div>
    <div class="contact-address">418 Colbrook Blvd.<br>Brenton, ON<br>K9R-3M5</div>
    <ul class="contact-lines">
      <li>
        <svg viewBox="0 0 14 14" aria-hidden="true"><rect x="3" y="0.5" width="8" height="13" rx="1.5" fill="none" stroke="#8a2423" stroke-width="1.6"/><rect x="6" y="10.5" width="2" height="1.4" fill="#8a2423"/></svg>
        (555) 214-3968
      </li>
      <li>
        <svg viewBox="0 0 14 14" aria-hidden="true"><rect x="0.5" y="3" width="13" height="9" fill="#8a2423"/><path d="M0.5 3 L7 8 L13.5 3" fill="none" stroke="#f7f7f7" stroke-width="1.2"/></svg>
        alexbernard@velkaflooring.com
      </li>
      <li>
        <svg viewBox="0 0 14 14" aria-hidden="true"><circle cx="7" cy="7" r="6.5" fill="#8a2423"/><path d="M4 4 Q6 5 5 7 Q7 8 6 11 M9 3 Q8 6 11 8" fill="none" stroke="#f7f7f7" stroke-width="1.2"/></svg>
        www.velkaflooring.com
      </li>
    </ul>
  </div>

  <svg class="card-band" viewBox="0 0 644 18" aria-hidden="true">
    <polygon points="0,0 476,0 472,18 0,18" fill="#8a2423"/>
    <polygon points="480,0 644,0 644,18 476,18" fill="#d6a623"/>
  </svg>
</section>

<section class="card card-back">
  <div class="brand">
    <div class="brand-name"><span class="brand-mark"></span>Velka</div>
    <div class="brand-tagline">Planchers &amp; Escaliers<br>Flooring &amp; Stairs</div>
  </div>
</section>

</body>
</html>
```